Help a start up law firm make an impression! - Website

We are a property development and conveyancing law firm looking for some to design our website. The initial brief is for 6 pages with scope for on-going work.

Law firms are traditionally quite conservative and we want to break the mold. We want to come across as fun and modern, while still being professional.

A good example is https://quorrantlaw.com.au/. It's professional yet modern.
Updates

Another good site I like in the same industry: https://www.tindalemarshconveyancing.com.au/

Target Market(s)

Tech savy home buyers and sellers - generally 30 to 50 years old

Industry/Entity Type

Law Firm

Coding

Coded - Design and coding required

Number of Pages Required

5+ page

Font styles to use
Other font styles liked:
• No idea

Colors
f04a50

Requirements
Must have
• The elements set out in the design brief document

```html
<!DOCTYPE html>
<html lang="en">
<head>
<meta charset="utf-8">
<title>Harcastle Law</title>
<link rel="stylesheet" href="https://fonts.googleapis.com/css2?family=Roboto:wght@300;400;500;700&display=swap">
<style>
:root{
  --rose:#d8405c;
  --rose-dark:#b8334c;
  --ink:#111111;
  --text:#333333;
  --muted:#777777;
  --white:#ffffff;
  --band:#f1f1f1;
}
*{box-sizing:border-box;margin:0;padding:0}
html,body{width:1200px;height:4455px;overflow:hidden;background:var(--white)}
body{font-family:'Roboto',Arial,sans-serif;color:var(--text)}
.page{position:relative;width:1200px;height:4455px;overflow:hidden}
section,header,footer{position:relative;width:1200px;overflow:hidden}
.abs{position:absolute}
.photo{position:absolute}
.accent{color:var(--rose)}
.section-title{position:absolute;left:0;width:1200px;text-align:center;font-weight:300;font-size:38px;color:var(--ink)}

/* hero */
.hero{height:648px;background:linear-gradient(160deg,#cfd3d6 0%,#9aa1a6 45%,#5d646a 100%)}
.hero .photo{inset:0;background:linear-gradient(180deg,rgba(40,44,48,.15),rgba(30,32,36,.45))}
.nav{position:absolute;top:26px;left:178px;display:flex;gap:0;align-items:center}
.nav a{color:var(--white);text-decoration:none;font-size:16px;padding:0 19px;border-right:1px solid rgba(255,255,255,.6);line-height:30px}
.nav a:last-child{border-right:0}
.search{position:absolute;left:988px;top:24px;width:134px;height:36px;border-radius:18px;background:var(--rose);display:flex;align-items:center;padding-left:14px;color:var(--white);font-size:14px}
.search span.go{position:absolute;right:3px;top:3px;width:30px;height:30px;border-radius:50%;background:var(--ink)}
.brand{position:absolute;top:140px;left:0;width:1200px;text-align:center;font-size:64px;font-weight:700;color:var(--white);letter-spacing:-1px}
.hero-title{position:absolute;top:266px;left:0;width:1200px;text-align:center;color:var(--white);font-weight:700;font-size:38px;line-height:42px;text-transform:uppercase}
.btn{display:inline-flex;align-items:center;justify-content:center;font-size:19px;text-transform:uppercase;text-decoration:none;position:absolute}
.btn-rose{background:var(--rose);color:var(--white)}
.btn-white{background:var(--white);color:var(--rose)}
.btn-black{background:var(--ink);color:var(--white)}
.dots{position:absolute;top:592px;left:546px;display:flex;gap:6px}
.dots i{width:16px;height:16px;border:2px solid #ccc;background:rgba(255,255,255,.6);display:block}
.dots i.on{background:var(--rose);border-color:var(--white)}

/* about */
.about{height:421px}
.feature{position:absolute;top:157px;width:220px;text-align:center}
.feature .ring{width:148px;height:148px;margin:0 auto}
.feature p{margin-top:34px;color:var(--rose);font-size:15px;text-transform:uppercase}

/* conveyancing */
.convey{height:523px;background:var(--ink)}
.convey .photo{left:0;top:0;width:600px;height:523px;background:linear-gradient(135deg,#f2f3f5 0%,#c9ced3 55%,#8d959c 100%)}
.convey h2{position:absolute;left:642px;top:46px;font-weight:400;font-size:40px;color:var(--rose)}
.convey .lead{position:absolute;left:642px;top:108px;width:500px;font-size:15px;line-height:22px;color:var(--white)}
.convey .links{position:absolute;left:642px;top:164px;display:flex;gap:40px;font-size:19px;color:var(--rose);text-transform:uppercase}
.convey .links span{border-bottom:2px solid var(--rose);padding-bottom:3px}
.field{position:absolute;height:53px;border:1px solid #777;color:var(--white);font-size:14px;display:flex;align-items:center;padding-left:12px}
.convey .offer{position:absolute;left:642px;top:320px;width:500px;font-size:18px;line-height:28px;color:var(--white)}

/* development */
.develop{height:523px;background:var(--rose)}
.develop .photo{left:600px;top:0;width:600px;height:523px;background:linear-gradient(180deg,#eef0f3 0%,#b8c0c8 55%,#6a737c 100%)}
.develop h2{position:absolute;left:80px;top:56px;font-weight:400;font-size:40px;color:var(--white)}
.develop ul{position:absolute;left:80px;top:128px;width:480px;list-style:none;color:var(--white);font-size:19px;line-height:26px}
.develop li{position:relative;padding-left:44px;margin-bottom:22px}
.develop li svg{position:absolute;left:0;top:6px}

/* team */
.team{height:475px}
.member{position:absolute;top:142px;width:180px;text-align:center}
.member .portrait{width:146px;height:146px;border-radius:50%;margin:0 auto;border:4px solid #eee;background:linear-gradient(160deg,#d9d9d9,#9c9c9c)}
.member h3{margin-top:44px;font-size:15px;font-weight:400;color:var(--rose);text-transform:uppercase}
.member p{margin-top:7px;font-size:12px;color:var(--muted);text-transform:uppercase}
.member .social{margin-top:14px;display:flex;justify-content:center;gap:12px}
.member .social i{width:11px;height:11px;border-radius:50%;background:var(--ink);display:block}

/* testimonials */
.voices{height:404px;background:linear-gradient(135deg,#e05a73 0%,#c9405b 60%,#b03350 100%)}
.voices .photo{inset:0;background:linear-gradient(90deg,rgba(255,255,255,.06),rgba(0,0,0,.08),rgba(255,255,255,.06))}
.voices .section-title{color:var(--white);top:60px}
.avatar{position:absolute;top:157px;width:140px;height:140px;border-radius:50%;border:5px solid var(--white);background:linear-gradient(160deg,#f0e2dc,#b89a90)}
.quote-name{position:absolute;top:155px;font-size:17px;color:var(--white)}
.quote-box{position:absolute;top:187px;height:125px;border:2px solid rgba(255,255,255,.85);padding:16px 18px 0 36px;color:var(--white);font-size:15px;line-height:20px}
.quote-box b{position:absolute;left:12px;top:10px;font-size:30px}

/* blog */
.blog{height:511px}
.blog .intro{position:absolute;top:130px;left:200px;width:800px;text-align:center;font-size:15px;line-height:26px;color:var(--muted)}
.post{position:absolute;top:208px;height:219px;background:var(--rose)}
.post .photo{left:0;top:0;width:270px;height:219px;background:linear-gradient(150deg,#e8eaed,#9ba2a9)}
.post .date{position:absolute;left:250px;top:0;width:52px;height:70px;background:var(--ink);color:var(--white);text-align:center;font-size:24px;line-height:30px;padding-top:6px}
.post .date small{display:block;font-size:14px;line-height:18px}
.post h3{position:absolute;left:300px;top:8px;width:190px;font-weight:400;font-size:24px;line-height:27px;color:var(--white)}
.post p{position:absolute;left:300px;top:74px;width:170px;font-size:15px;line-height:20px;color:var(--white)}
.post .more{position:absolute;left:300px;top:174px;font-size:14px;color:var(--white);display:flex;align-items:center;gap:10px}

/* partners */
.partners{height:142px;background:var(--band)}
.badge{position:absolute;top:30px;width:140px;height:82px;border:3px solid var(--rose);border-radius:6px}
.badge.round{width:86px;height:86px;border-radius:50%;top:28px}

/* map */
.map{height:267px;background:linear-gradient(120deg,#e9ebe7 0%,#dcdfda 50%,#e6e4dc 100%)}
.map-card{position:absolute;left:80px;top:14px;width:238px;height:88px;background:var(--white);padding:12px 14px;font-size:14px;line-height:18px;box-shadow:0 1px 4px rgba(0,0,0,.25)}
.map-card strong{color:var(--rose);font-weight:400}

/* contact */
.contact{height:452px;background:linear-gradient(135deg,#e1566f 0%,#cf4460 60%,#bd3753 100%)}
.mail-badge{position:absolute;left:567px;top:-33px;width:66px;height:66px;border-radius:50%;background:var(--ink);z-index:2;display:flex;align-items:center;justify-content:center;border:3px solid var(--white)}
.input{position:absolute;background:var(--white);color:#888;font-size:14px;padding:8px 12px}
.contact-line{position:absolute;top:353px;display:flex;align-items:center;gap:14px;color:var(--white);font-size:15px;line-height:20px}

/* footer */
.site-footer{height:89px;background:var(--rose-dark);color:var(--white)}
.site-footer .copy{position:absolute;left:80px;top:22px;font-size:14px;line-height:20px}
.site-footer .links{position:absolute;right:78px;top:42px;font-size:14px;display:flex}
.site-footer .links span{padding:0 9px;border-right:1px solid rgba(255,255,255,.7)}
.site-footer .links span:last-child{border-right:0;padding-right:0}
</style>
</head>
<body>
<div class="page">

<header class="hero">
  <div class="photo" role="img" aria-label="Photo of lawyers meeting around a boardroom table"></div>
  <nav class="nav">
    <a href="#">Home</a><a href="#">Who We Are</a><a href="#">What We Do</a><a href="#">Where We Work</a><a href="#">Careers</a><a href="#">News</a><a href="#">Contact</a>
  </nav>
  <div class="search">Search...<span class="go"></span></div>
  <div class="brand">Harcastle Law</div>
  <h1 class="hero-title">Guiding successful<br>resolutions, quickly and<br>intelligently</h1>
  <a class="btn btn-rose" style="left:386px;top:420px;width:205px;height:55px">Learn More</a>
  <a class="btn btn-white" style="left:603px;top:420px;width:208px;height:55px">Contact Us</a>
  <div class="dots"><i></i><i></i><i class="on"></i><i></i><i></i></div>
</header>

<section class="about">
  <h2 class="section-title" style="top:70px">About <span class="accent">Harcastle Law</span></h2>
  <div class="feature" style="left:181px">
    <svg class="ring" viewBox="0 0 148 148"><circle cx="74" cy="74" r="70" fill="#fff" stroke="#d8405c" stroke-width="6"/><path d="M4 74a70 70 0 0 0 140 0z" fill="#d8405c"/><circle cx="74" cy="62" r="18" fill="none" stroke="#111" stroke-width="3"/><path d="M46 96h56" stroke="#111" stroke-width="3"/></svg>
    <p>Cost Certaint</p>
  </div>
  <div class="feature" style="left:386px">
    <svg class="ring" viewBox="0 0 148 148"><circle cx="74" cy="74" r="70" fill="#fff" stroke="#d8405c" stroke-width="6"/><path d="M4 74a70 70 0 0 0 140 0z" fill="#d8405c"/><path d="M44 56h60M74 40v56M54 56l-10 20h20zM94 56l-10 20h20zM56 96h36" fill="none" stroke="#111" stroke-width="3"/></svg>
    <p>Expert Lawyers</p>
  </div>
  <div class="feature" style="left:591px">
    <svg class="ring" viewBox="0 0 148 148"><circle cx="74" cy="74" r="70" fill="#fff" stroke="#d8405c" stroke-width="6"/><path d="M4 74a70 70 0 0 0 140 0z" fill="#d8405c"/><rect x="44" y="46" width="50" height="36" fill="none" stroke="#111" stroke-width="3"/><rect x="86" y="62" width="20" height="34" fill="#fff" stroke="#111" stroke-width="3"/><path d="M58 92h26" stroke="#111" stroke-width="3"/></svg>
    <p>Responsive Service</p>
  </div>
  <div class="feature" style="left:796px">
    <svg class="ring" viewBox="0 0 148 148"><circle cx="74" cy="74" r="70" fill="#fff" stroke="#d8405c" stroke-width="6"/><path d="M4 74a70 70 0 0 0 140 0z" fill="#d8405c"/><circle cx="60" cy="48" r="8" fill="#111"/><circle cx="88" cy="48" r="8" fill="#111"/><path d="M50 98V66h20l8 10 10-10v32" fill="none" stroke="#111" stroke-width="3"/></svg>
    <p>Commercial Advice</p>
  </div>
</section>

<section class="convey">
  <div class="photo" role="img" aria-label="Photo of hands reviewing documents on a tablet"></div>
  <h2>Conveyancing</h2>
  <p class="lead"><span class="accent">Harcastle Law</span> property conveyancing done quickly &amp; easily for a fixed fair fee – that's our client-care guarantee.</p>
  <div class="links"><span>Guide to Buy</span><span>Guide to Sell</span></div>
  <div class="field" style="left:642px;top:1307px;top:238px;width:216px">Name* :</div>
  <div class="field" style="left:864px;top:238px;width:214px">Email* :</div>
  <div class="abs" style="left:1087px;top:238px;width:71px;height:53px;background:var(--rose);display:flex;align-items:center;justify-content:center">
    <svg width="24" height="24" viewBox="0 0 24 24"><circle cx="10" cy="10" r="7" fill="none" stroke="#fff" stroke-width="2"/><path d="M15 15l6 6" stroke="#fff" stroke-width="2"/></svg>
  </div>
  <p class="offer">Receive a 10% discount on your conveyancing in under 30 seconds.</p>
  <a class="btn btn-rose" style="left:642px;top:398px;width:207px;height:53px">I´m Selling</a>
  <a class="btn btn-rose" style="left:858px;top:398px;width:208px;height:53px">I´m Buying</a>
</section>

<section class="develop">
  <h2>Property Development</h2>
  <ul>
    <li><svg width="26" height="16" viewBox="0 0 26 16"><path d="M0 0l26 8L0 16l7-8z" fill="#111"/></svg>Specialist property development lawyers</li>
    <li><svg width="26" height="16" viewBox="0 0 26 16"><path d="M0 0l26 8L0 16l7-8z" fill="#111"/></svg>Flexible fee arrangements</li>
    <li><svg width="26" height="16" viewBox="0 0 26 16"><path d="M0 0l26 8L0 16l7-8z" fill="#111"/></svg>Commercial advice</li>
    <li><svg width="26" height="16" viewBox="0 0 26 16"><path d="M0 0l26 8L0 16l7-8z" fill="#111"/></svg>Integrated Development Management and Project Marketing services</li>
  </ul>
  <a class="btn btn-black" style="left:77px;top:371px;width:208px;height:54px">Learn More</a>
  <div class="photo" role="img" aria-label="Photo of a city skyline with high-rise towers by a river"></div>
</section>

<section class="team">
  <h2 class="section-title" style="top:58px">Meet Our <span class="accent">Team</span></h2>
  <div class="member" style="left:67px"><div class="portrait" role="img" aria-label="Portrait of Owen Fairbrook"></div><h3>Owen Fairbrook</h3><p>Senior Partner</p><div class="social"><i></i><i></i><i></i><i></i></div></div>
  <div class="member" style="left:257px"><div class="portrait" role="img" aria-label="Portrait of Tessa Quill"></div><h3>Tessa Quill</h3><p>Senior Partner</p><div class="social"><i></i><i></i><i></i><i></i></div></div>
  <div class="member" style="left:421px"><div class="portrait" role="img" aria-label="Portrait of Felix Marden"></div><h3>Felix Marden</h3><p>Senior Partner</p><div class="social"><i></i><i></i><i></i><i></i></div></div>
  <div class="member" style="left:590px"><div class="portrait" role="img" aria-label="Portrait of Curtis Penhale"></div><h3>Curtis Penhale</h3><p>Senior Partner</p><div class="social"><i></i><i></i><i></i><i></i></div></div>
  <div class="member" style="left:759px"><div class="portrait" role="img" aria-label="Portrait of Rosa Whitcombe"></div><h3>Rosa Whitcombe</h3><p>Senior Partner</p><div class="social"><i></i><i></i><i></i><i></i></div></div>
  <div class="member" style="left:946px"><div class="portrait" role="img" aria-label="Portrait of Ines Dalby"></div><h3>Ines Dalby</h3><p>Senior Partner</p><div class="social"><i></i><i></i><i></i><i></i></div></div>
</section>

<section class="voices">
  <div class="photo" role="img" aria-label="Rose-tinted collage of client photos"></div>
  <h2 class="section-title">What Our <span style="color:#fff">Client Say</span></h2>
  <div class="avatar" style="left:74px" role="img" aria-label="Portrait of Mira Tolland"></div>
  <div class="quote-name" style="left:240px">Mira Tolland &nbsp;|&nbsp; Customer</div>
  <div class="quote-box" style="left:238px;width:350px"><b>“</b>Lorem Ipsum is simply dummy text of the printing and typesetting industry. Lorem Ipsum has been the industry's standard dummy text ever since the 1500s.</div>
  <div class="avatar" style="left:627px" role="img" aria-label="Portrait of Reid Calloway"></div>
  <div class="quote-name" style="left:787px">Reid Calloway &nbsp;|&nbsp; Customer</div>
  <div class="quote-box" style="left:781px;width:342px"><b>“</b>Lorem Ipsum is simply dummy text of the printing and typesetting industry. Lorem Ipsum has been the industry's standard dummy text ever since the 1500s.</div>
</section>

<section class="blog">
  <h2 class="section-title" style="top:62px">Recent <span class="accent">Blog</span></h2>
  <p class="intro">Lorem Ipsum is simply dummy text of the printing and typesetting industry. Lorem Ipsum has been the industry's standard dummy text ever since the 1500s.</p>
  <article class="post" style="left:77px;width:505px">
    <div class="photo" role="img" aria-label="Photo of three lawyers standing in a library"></div>
    <div class="date">24<small>Oct</small></div>
    <h3>Lorem Ipsum is simply dummy</h3>
    <p>Lorem Ipsum is simply dummy text of the printing and typesetting</p>
    <div class="more">READ MORE <svg width="26" height="10" viewBox="0 0 26 10"><path d="M0 5h24M19 1l5 4-5 4" fill="none" stroke="#fff" stroke-width="2"/></svg></div>
  </article>
  <article class="post" style="left:624px;width:499px">
    <div class="photo" role="img" aria-label="Photo of colleagues discussing papers at a desk"></div>
    <div class="date">24<small>Oct</small></div>
    <h3>Lorem Ipsum is simply dummy</h3>
    <p>Lorem Ipsum is simply dummy text of the printing and typesetting</p>
    <div class="more">READ MORE <svg width="26" height="10" viewBox="0 0 26 10"><path d="M0 5h24M19 1l5 4-5 4" fill="none" stroke="#fff" stroke-width="2"/></svg></div>
  </article>
</section>

<section class="partners">
  <div class="badge" style="left:80px"></div>
  <div class="badge" style="left:262px;border-width:0;border-bottom-width:3px;border-radius:0"></div>
  <div class="badge round" style="left:480px"></div>
  <div class="badge" style="left:625px;border-width:0;border-bottom-width:3px;border-radius:0"></div>
  <div class="badge round" style="left:842px"></div>
  <div class="badge" style="left:982px;border-radius:40px 40px 6px 6px"></div>
</section>

<section class="map">
  <div class="photo" style="inset:0" role="img" aria-label="Street map showing the office location"></div>
  <div class="map-card"><strong>Harcastle Law</strong><br>48 Harbour Lane<br>Brookvale</div>
</section>

<section class="contact" style="overflow:visible">
  <div class="mail-badge"><svg width="34" height="24" viewBox="0 0 34 24"><rect x="1" y="1" width="32" height="22" fill="#fff"/><path d="M1 1l16 12L33 1" fill="none" stroke="#111" stroke-width="2"/></svg></div>
  <div class="input" style="left:232px;top:81px;width:362px;height:42px">Name* :</div>
  <div class="input" style="left:232px;top:134px;width:362px;height:42px">Email* :</div>
  <div class="input" style="left:232px;top:187px;width:362px;height:42px">Phone* :</div>
  <div class="input" style="left:606px;top:81px;width:362px;height:148px">Comment :</div>
  <a class="btn btn-black" style="left:475px;top:250px;width:247px;height:50px">Submit</a>
  <div class="contact-line" style="left:223px">
    <svg width="30" height="24" viewBox="0 0 30 24"><path d="M2 4l8-3 10 3 8-3v19l-8 3-10-3-8 3z" fill="none" stroke="#fff" stroke-width="2"/></svg>
    <span>48 Harbour Lane<br>Brookvale, NSW 2100</span>
  </div>
  <div class="contact-line" style="left:520px">
    <svg width="22" height="22" viewBox="0 0 22 22"><path d="M4 2h5l2 5-3 2a12 12 0 0 0 5 5l2-3 5 2v5c0 1-1 2-2 2A18 18 0 0 1 2 4c0-1 1-2 2-2z" fill="none" stroke="#fff" stroke-width="2"/></svg>
    <span>1.800.000.4417</span>
  </div>
  <div class="contact-line" style="left:787px">
    <svg width="26" height="18" viewBox="0 0 26 18"><rect x="1" y="1" width="24" height="16" fill="none" stroke="#fff" stroke-width="2"/><path d="M1 1l12 9 12-9" fill="none" stroke="#fff" stroke-width="2"/></svg>
    <span>hello@harcastlelaw.com</span>
  </div>
</section>

<footer class="site-footer">
  <p class="copy">© Copyright - 2017<br>Harcastle Law &nbsp;|&nbsp; All Rights Reserved</p>
  <div class="links"><span>Home</span><span>Who we are</span><span>What we do</span><span>Where we are</span><span>Careers</span><span>News</span><span>Contact</span></div>
</footer>

</div>
</body>
</html>
```